Cover of the e-book award-winning national sports figure.

I would like to utilize the picture this attached to this brief. If you could pull the trophies and myself out and place with the new background, that’s what I would like to see . I would like to have a new bookcover design for my e-book. I attached below the original cover and have marked in red. The things that I don’t want on the new cover. I’ve attached a picture that’s not the original. I’m waiting on the high copy. I would like to replace the old logo with the one that I have attached. The website that I would like to have on the book is www.dellanvmoreaux.com.
Target Market(s)
Biography
Industry/Entity Type
Sports & motivation?
Requirements
Must have
- Picture of me in the blue suit on the cover the title of the book walking past midnight lessons from quiet harbors
Nice to have
- Utilize the old cover that I have attached for some ideas
Should not have
- The cover should not have anything related to marlow crest press Inc.

```html
<!DOCTYPE html>
<html lang="en">
<head>
<meta charset="utf-8">
<title>Walking Past Midnight – Book Cover</title>
<link href="https://fonts.googleapis.com/css2?family=Anton&family=Archivo+Black&family=Archivo:wght@700;800&display=swap" rel="stylesheet">
<style>
  :root{
    --page-bg:#d4d4d4;
    --satin-light:#eeeeee;
    --satin-mid:#d2d2d2;
    --ink:#1e1e1e;
    --slate:#4f616b;
    --slate-light:#5d717c;
    --night:#0e0e0e;
    --pale-blue:#a9c6d6;
    --accent-blue:#2f8fd0;
    --white:#ffffff;
    --suit:#2a4f9a;
  }
  *{margin:0;padding:0;box-sizing:border-box}
  html,body{width:1200px;height:675px;overflow:hidden}
  body{background:radial-gradient(ellipse at 50% 40%,#e6e6e6 0%,var(--page-bg) 70%);position:relative}

  .book-cover{
    position:absolute;left:380px;top:27px;width:440px;height:620px;
    background:linear-gradient(135deg,var(--satin-light) 0%,var(--satin-mid) 45%,#e4e4e4 70%,#cfcfcf 100%);
    overflow:hidden;
    box-shadow:0 18px 40px rgba(0,0,0,.25);
  }
  .cover-shapes{position:absolute;inset:0}

  .author-photo{
    position:absolute;left:250px;top:62px;width:185px;height:375px;
    background:linear-gradient(180deg,#b9c4d6 0%,var(--suit) 35%,#1d3b78 100%);
    border:5px solid var(--slate);
    border-radius:60px 20px 0 50px;
  }

  .title{
    position:absolute;left:28px;top:68px;
    font-family:"Anton",sans-serif;color:var(--ink);
    text-transform:uppercase;line-height:.95;
  }
  .title-line{display:block}
  .title-line--small{font-size:50px}
  .title-line--mid{font-size:50px}
  .title-line--large{font-size:76px;letter-spacing:-1px}

  .subtitle{
    position:absolute;left:128px;top:300px;
    background:var(--slate);color:var(--satin-light);
    padding:6px 12px 8px;
    font-family:"Archivo Black",sans-serif;font-size:19px;line-height:1.02;
  }

  .author-name{
    position:absolute;left:150px;top:408px;
    font-family:"Archivo",sans-serif;font-weight:800;font-size:25px;line-height:1.05;
    color:var(--ink);letter-spacing:.5px;
  }

  .foreword{
    position:absolute;left:172px;top:540px;
    font-family:"Archivo",sans-serif;font-weight:800;text-transform:uppercase;
  }
  .foreword-label{display:block;font-size:11px;color:var(--pale-blue);letter-spacing:1px}
  .foreword-name{display:block;font-size:24px;color:var(--white);letter-spacing:.5px}

  .brand-mark{
    position:absolute;left:318px;top:452px;
    display:flex;align-items:center;gap:8px;
    font-family:"Archivo",sans-serif;font-weight:800;font-size:12px;
    color:var(--pale-blue);text-transform:uppercase;letter-spacing:.5px;
  }
  .brand-dot{width:20px;height:20px;border-radius:50%;background:var(--accent-blue)}
</style>
</head>
<body>
  <main class="book-cover">
    <svg class="cover-shapes" viewBox="0 0 440 620" width="440" height="620" aria-hidden="true">
      <path d="M440 250 C 360 290 300 360 260 440 C 220 520 120 560 0 560 L0 620 L440 620 Z" fill="var(--slate-light)"/>
      <path d="M440 395 C 360 400 300 430 260 490 C 220 560 150 600 100 620 L440 620 Z" fill="var(--night)"/>
    </svg>

    <div class="author-photo" role="img" aria-label="Portrait of the author standing in a blue pinstripe suit with a patterned tie, smiling, hand in pocket"></div>

    <h1 class="title">
      <span class="title-line title-line--small">Walking</span>
      <span class="title-line title-line--mid">Past</span>
      <span class="title-line title-line--large">Midnight</span>
    </h1>

    <p class="subtitle">Lessons From<br>Quiet<br>Harbors</p>

    <p class="author-name">DELLAN<br>MOREAUX</p>

    <div class="brand-mark"><span class="brand-dot"></span>Dellan Moreaux</div>

    <p class="foreword">
      <span class="foreword-label">Forward by</span>
      <span class="foreword-name">Corwin Ashby</span>
    </p>
  </main>
</body>
</html>
```